Investment company seeks website design

TBW (Tallowbrook Wealth Partners) are an investment company that actively targets and acquires businesses and grows them after acquisition.

The website design needs to be professional and should communicate to key decision-makers inside the acquirable companies that TBW targets.

You will design the Homepage initially for the competition. If you win the competition, you will design the inner pages too.

More details are attached below.

Target Market(s)

Business owners and decision makers inside acquirable companies

Industry/Entity Type

Company Investment

Number of Pages Required

5+ page

Requirements
Must have
• High Attention to Detail. Following the Wireframes closely. Consistent colour and design choices
Should not have
• Anything cheap, too bright or untidy

```html
<!DOCTYPE html>
<html lang="en">
<head>
<meta charset="utf-8">
<title>Tallowbrook Wealth Partners — Homepage</title>
<link href="https://fonts.googleapis.com/css2?family=Inter:wght@300;400;500;600;700&display=swap" rel="stylesheet">
<style>
:root{
  --green:#7bb542;
  --navy:#203457;
  --navy-deep:#1a2744;
  --slate:#6c7888;
  --mist:#e1e2e3;
  --paper:#f9f9f9;
  --board:#cbcbcb;
  --ink:#203457;
  --muted:#7a8494;
  --white:#ffffff;
}
*{box-sizing:border-box;margin:0;padding:0}
html,body{width:1200px;height:3062px;overflow:hidden}
body{background:var(--board);font-family:"Inter",Arial,sans-serif;color:var(--ink);position:relative}

/* brand board */
.brand-board{position:absolute;left:0;top:0;width:1200px;height:230px}
.brand-name{position:absolute;left:181px;top:112px;display:flex;align-items:center;gap:12px;font-size:22px;font-weight:400;color:var(--navy);letter-spacing:.5px}
.brand-name .mark{width:34px;height:34px;background:var(--navy)}
.board-label{position:absolute;font-size:24px;font-weight:400;color:var(--navy)}
.font-name{position:absolute;left:549px;top:143px;font-size:15px;color:var(--slate)}
.swatch{position:absolute;top:132px;width:42px;height:42px;border-radius:50%}
.swatch span{position:absolute;top:50px;left:50%;transform:translateX(-50%);font-size:9.5px;color:#444;white-space:nowrap}

/* site */
.site{position:absolute;left:210px;top:276px;width:783px;background:var(--white);overflow:hidden}
.section{position:relative;width:783px}
.photo{position:absolute}

/* hero */
.hero{height:402px;background:linear-gradient(180deg,#152846 0%,#243d64 45%,#3b5677 100%)}
.hero .photo{inset:0;background:radial-gradient(ellipse at 40% 75%,rgba(170,150,125,.45),transparent 45%),radial-gradient(ellipse at 82% 35%,rgba(140,130,110,.35),transparent 35%),linear-gradient(180deg,rgba(20,35,62,.2),rgba(50,75,110,.35))}
.nav{position:absolute;left:0;top:0;width:783px;height:48px;display:flex;align-items:center;padding:0 54px 0 102px;border-bottom:1px solid rgba(255,255,255,.12);background:rgba(20,36,64,.35)}
.nav-brand{display:flex;align-items:center;gap:8px;font-size:11px;font-weight:500;color:var(--white);letter-spacing:.3px}
.nav-brand .mark{width:14px;height:14px;background:var(--green)}
.nav-links{display:flex;gap:26px;margin-left:auto;font-size:7.5px;color:rgba(255,255,255,.85)}
.nav-cta{margin-left:20px;padding-left:20px;border-left:1px solid rgba(255,255,255,.25);height:48px;display:flex;align-items:center;gap:6px;font-size:7.5px;font-weight:600;color:var(--white)}
.hero-title{position:absolute;top:181px;font-size:29px;font-weight:500;line-height:34px;color:var(--white);letter-spacing:-.3px}
.hero-title em{font-style:normal;color:var(--green)}
.hero-title.left{left:102px}
.hero-title.right{right:102px;text-align:right}
.hero-frame{position:absolute;left:227px;top:261px;width:329px;height:24px;border:1px solid rgba(255,255,255,.55);border-top:none}
.btn-solid{position:absolute;display:flex;align-items:center;justify-content:center;gap:6px;background:var(--green);color:var(--white);font-size:7.5px;font-weight:600}
.hero .btn-solid{left:345px;top:273px;width:97px;height:29px}

/* about */
.about{height:396px}
.about h2{position:absolute;left:102px;top:66px;font-size:24px;font-weight:400;line-height:29px;color:var(--navy)}
.about-copy{position:absolute;left:102px;top:138px;width:250px;padding-left:9px;border-left:1px solid var(--green);font-size:8px;line-height:13px;color:var(--muted)}
.services-label{position:absolute;left:103px;top:198px;font-size:9px;font-weight:600;color:var(--navy)}
.services{position:absolute;left:103px;top:219px;list-style:none;font-size:7.8px;color:var(--muted)}
.services li{height:15.5px;display:flex;align-items:center;gap:6px}
.dot{width:5px;height:5px;border-radius:50%;background:var(--green);flex:none}
.btn-outline{position:absolute;left:102px;top:301px;width:109px;height:28px;border:1px solid var(--green);display:flex;align-items:center;justify-content:center;gap:5px;font-size:7.5px;font-weight:600;color:var(--navy)}
.about .accent-square{position:absolute;left:385px;top:50px;width:68px;height:45px;background:#eef0f3}
.about .photo{left:400px;top:64px;width:281px;height:282px;background:linear-gradient(160deg,#eef1f4 0%,#dfe5ea 55%,#b9c6d2 100%)}

/* qualities */
.qualities{height:348px;background:#f3f4f6}
.section-title{position:absolute;left:0;width:783px;text-align:center;font-size:24px;font-weight:400;color:var(--navy)}
.qualities .section-title{top:44px}
.q-card{position:absolute;width:275px;height:88px;background:var(--white);display:flex;gap:12px;padding:8px}
.q-icon{width:74px;height:72px;background:var(--navy);flex:none;display:flex;align-items:center;justify-content:center}
.q-body h3{font-size:9px;font-weight:500;color:var(--navy);margin:7px 0 6px}
.q-body ul{list-style:none;font-size:7px;color:var(--muted)}
.q-body li{height:14px;display:flex;align-items:center;gap:5px}
.q-body .dot{width:4px;height:4px}

/* explore */
.explore{height:214px;background:linear-gradient(100deg,#213a63 0%,#2c4a78 45%,#203457 100%)}
.explore .photo{inset:0;background:radial-gradient(ellipse at 60% 65%,rgba(120,145,185,.35),transparent 50%)}
.explore .section-title{top:42px;color:var(--white)}
.explore p{position:absolute;left:0;top:88px;width:783px;text-align:center;font-size:8px;line-height:13px;color:rgba(255,255,255,.75)}
.explore .btn-solid{left:342px;top:135px;width:98px;height:28px}

/* process */
.process{height:352px}
.process .section-title{top:44px}
.step-label{position:absolute;top:101px;width:150px;text-align:center;font-size:9.5px;font-weight:500;line-height:13px;color:var(--navy)}
.step{position:absolute;top:153px;width:149px;height:149px;border-radius:50%;display:flex;align-items:center;justify-content:center;text-align:center;padding:0 28px;font-size:8.5px;line-height:13px}
.step.one{background:#eeeeef;color:var(--muted)}
.step.two{background:var(--navy);color:rgba(255,255,255,.9)}
.step.three{background:var(--green);color:rgba(255,255,255,.9)}
.step-arrow{position:absolute;top:214px}
.process .rule{position:absolute;left:102px;right:102px;bottom:0;height:1px;background:#e4e6ea}

/* insights */
.insights-head{height:99px}
.insights-head .section-title{top:40px}
.insights{height:297px}
.news-card{position:absolute;top:0;height:297px;overflow:hidden}
.news-card .photo{inset:0}
.news-card .shade{position:absolute;inset:0;background:linear-gradient(180deg,rgba(32,52,87,0) 45%,rgba(32,52,87,.92) 100%)}
.news-date{position:absolute;left:19px;top:228px;font-size:7px;letter-spacing:1.3px;color:var(--green)}
.news-title{position:absolute;left:19px;top:242px;width:150px;font-size:10.5px;font-weight:600;line-height:14px;color:var(--white)}

/* balance */
.balance{height:335px;background:linear-gradient(180deg,#f2f3f4,#e6e8ea)}
.balance .photo.city{right:0;top:0;width:240px;height:335px;background:linear-gradient(180deg,#dfe2e5 0%,#b7bdc3 70%,#8a9096 100%)}
.balance .photo.rail{left:0;bottom:0;width:783px;height:55px;background:linear-gradient(90deg,rgba(225,226,227,0) 0%,rgba(120,125,130,.45) 100%)}
.pillar{position:absolute;left:102px;width:85px;height:33px;background:var(--white);display:flex;align-items:center;justify-content:center;font-size:7px;font-weight:600;letter-spacing:1.3px;color:var(--navy)}
.pillar-lines{position:absolute;left:0;top:0}
.balance-panel{position:absolute;left:266px;top:68px;width:397px;height:218px;background:var(--navy)}
.balance-panel .kicker{position:absolute;left:50px;top:78px;font-size:8.5px;letter-spacing:3.6px;color:rgba(255,255,255,.85)}
.balance-panel h2{position:absolute;left:50px;top:95px;font-size:25px;font-weight:300;line-height:29px;color:var(--white)}
.balance-panel h2 em{font-style:normal;font-weight:500;color:var(--green)}
.balance .photo.figure{left:600px;top:20px;width:110px;height:285px;border-radius:40px;background:linear-gradient(180deg,rgba(60,70,90,.35),rgba(32,52,87,.55))}

/* footer */
.footer{height:240px;background:var(--navy-deep)}
.footer-links{position:absolute;left:102px;top:48px;list-style:none;font-size:13.5px;font-weight:300;color:var(--white)}
.footer-links li{height:32px}
.footer-col{position:absolute;top:48px}
.footer-col h4{font-size:13.5px;font-weight:600;color:var(--white);margin-bottom:10px}
.footer-col .contact{display:inline-block;font-size:7.5px;color:var(--white);padding-bottom:3px;border-bottom:1px solid var(--green);margin-bottom:12px}
.footer-col address{font-style:normal;font-size:7px;line-height:13.5px;color:rgba(255,255,255,.45)}
.footer-base{position:absolute;left:102px;right:102px;top:186px;display:flex;justify-content:space-between;font-size:6.5px;color:rgba(255,255,255,.6)}
</style>
</head>
<body>

<header class="brand-board">
  <div class="brand-name"><span class="mark"></span>Tallowbrook Wealth Partners</div>
  <div class="board-label" style="left:549px;top:97px">Fonts:</div>
  <div class="font-name">Suisse Int'l</div>
  <div class="board-label" style="left:778px;top:97px">Colors:</div>
  <div class="swatch" style="left:778px;background:var(--green)"><span>#7bb542</span></div>
  <div class="swatch" style="left:828px;background:var(--navy)"><span>#203457</span></div>
  <div class="swatch" style="left:878px;background:var(--slate)"><span>#6c7888</span></div>
  <div class="swatch" style="left:929px;background:var(--mist)"><span>#e1e2e3</span></div>
  <div class="swatch" style="left:978px;background:var(--paper)"><span>#f9f9f9</span></div>
</header>

<main class="site">

  <section class="section hero">
    <div class="photo" role="img" aria-label="Hand balancing a wooden seesaw with stacked coins on a deep blue backdrop"></div>
    <nav class="nav">
      <div class="nav-brand"><span class="mark"></span>Tallowbrook Wealth Partners</div>
      <div class="nav-links"><span>Our Approach</span><span>Investment Criteria</span><span>About Us</span><span>Our Approach</span></div>
      <div class="nav-cta">
        <svg width="8" height="6" viewBox="0 0 8 6"><rect width="8" height="6" fill="#7bb542"/><path d="M0 0 L4 3 L8 0" stroke="#203457" stroke-width=".8" fill="none"/></svg>
        Email Us
      </div>
    </nav>
    <h1 class="hero-title left">The Very Best <em>Exit</em><br>for You</h1>
    <h1 class="hero-title right">The Best <em>Future</em> for<br>Your Business</h1>
    <div class="hero-frame"></div>
    <a class="btn-solid">Discover TBW
      <svg width="9" height="6" viewBox="0 0 9 6"><path d="M0 3H8M5.5 .5L8 3 5.5 5.5" stroke="#fff" stroke-width=".9" fill="none"/></svg>
    </a>
  </section>

  <section class="section about">
    <h2>We Will Make Your<br>Business Thrive</h2>
    <p class="about-copy">TBW is commited to helping businesses achieve significant growth. Under our stewardship, companies have the benefit of an experienced team expert to ensure that every company achieves their full potential</p>
    <div class="services-label">Our services include:</div>
    <ul class="services">
      <li><span class="dot"></span>Crafting long-term growth</li>
      <li><span class="dot"></span>Streamlining operations for maximum efficiency</li>
      <li><span class="dot"></span>Optimizing financial structures for expansion</li>
      <li><span class="dot"></span>Facilitating strategic-mergers and acquisitions</li>
    </ul>
    <a class="btn-outline">Unlock Your Potential
      <svg width="9" height="6" viewBox="0 0 9 6"><path d="M0 3H8M5.5 .5L8 3 5.5 5.5" stroke="#203457" stroke-width=".9" fill="none"/></svg>
    </a>
    <div class="accent-square"></div>
    <div class="photo" role="img" aria-label="Business team meeting in a bright office with blue lounge chairs"></div>
  </section>

  <section class="section qualities">
    <h2 class="section-title">Our Qualities &amp; Capabilities</h2>

    <div class="q-card" style="left:102px;top:96px">
      <div class="q-icon"><svg width="34" height="30" viewBox="0 0 34 30" fill="none" stroke="#fff" stroke-width="1"><circle cx="10" cy="5" r="3"/><circle cx="17" cy="5" r="3"/><circle cx="24" cy="5" r="3"/><path d="M5 14c0-3 2-5 5-5s5 2 5 5M12 14c0-3 2-5 5-5s5 2 5 5M19 14c0-3 2-5 5-5s5 2 5 5"/><path d="M2 22h8l6 2h8l6-4M2 27h10l8 1 12-6"/></svg></div>
      <div class="q-body"><h3>Driving Value</h3><ul><li><span class="dot"></span>Comprehensive long-term plan</li><li><span class="dot"></span>Ownership of company performance</li><li><span class="dot"></span>Vast experience in driving transformation</li></ul></div>
    </div>

    <div class="q-card" style="left:407px;top:96px">
      <div class="q-icon"><svg width="34" height="30" viewBox="0 0 34 30" fill="none" stroke="#fff" stroke-width="1"><circle cx="17" cy="5" r="3"/><path d="M12 13c0-3 2-5 5-5s5 2 5 5"/><circle cx="7" cy="19" r="3"/><path d="M2 28c0-3 2-5 5-5s5 2 5 5"/><circle cx="27" cy="19" r="3"/><path d="M22 28c0-3 2-5 5-5s5 2 5 5"/><path d="M13 15l-4 3M21 15l4 3M11 22h12"/></svg></div>
      <div class="q-body"><h3>Integrated Team</h3><ul><li><span class="dot"></span>Partnership culture</li><li><span class="dot"></span>Consistent senior team</li><li><span class="dot"></span>Detailed industry and operating experience</li></ul></div>
    </div>

    <div class="q-card" style="left:102px;top:209px">
      <div class="q-icon"><svg width="38" height="26" viewBox="0 0 38 26" fill="none" stroke="#fff" stroke-width="1"><path d="M1 6l7-3 5 4 6-2 6 2 5-4 7 3M1 6l4 10 5 4 4 3 3-1 3 2 3-2 4-1 4-4 4-11M13 7l-3 5 4 2 5-4 6 6M14 19l3 2M17 16l4 3M21 14l4 3"/></svg></div>
      <div class="q-body"><h3>Partnership with Management</h3><ul><li><span class="dot"></span>Strong, trust-based relationships</li><li><span class="dot"></span>Significant commitment of time on-the-ground</li><li><span class="dot"></span>Ability to take interim roles if needed</li></ul></div>
    </div>

    <div class="q-card" style="left:407px;top:209px">
      <div class="q-icon"><svg width="32" height="32" viewBox="0 0 32 32" fill="none" stroke="#fff" stroke-width="1"><path d="M28 4c-8 0-14 5-18 13l5 5c8-4 13-10 13-18z"/><circle cx="20" cy="12" r="2.5"/><path d="M10 17l-5 1 4-6 5-1M15 22l-1 5 6-4 1-5M8 21l-5 8M11 24l-5 6M6 19l-4 5"/></svg></div>
      <div class="q-body"><h3>Accelerated Excecution</h3><ul><li><span class="dot"></span>Relentless focus on priorities</li><li><span class="dot"></span>Drive through to results</li><li><span class="dot"></span>Commited to continuous development</li></ul></div>
    </div>
  </section>

  <section class="section explore">
    <div class="photo" role="img" aria-label="Two businesspeople shaking hands, tinted navy"></div>
    <h2 class="section-title">Explore Your Next Move</h2>
    <p>If you are looking for a change, then TBW can help you map out a smooth transition, and give<br>you the confidence that your company is in safe hands.</p>
    <a class="btn-solid">Discuss with TBW
      <svg width="9" height="6" viewBox="0 0 9 6"><path d="M0 3H8M5.5 .5L8 3 5.5 5.5" stroke="#fff" stroke-width=".9" fill="none"/></svg>
    </a>
  </section>

  <section class="section process">
    <h2 class="section-title">How TBW Will Transform Your Company</h2>
    <div class="step-label" style="left:102px">Discover Growth<br>Opportunities</div>
    <div class="step-label" style="left:317px">Craft Strategic<br>Solutions</div>
    <div class="step-label" style="left:532px">Drive Future<br>Success</div>
    <div class="step one" style="left:102px">Identify hidden growth opportunities for your business</div>
    <svg class="step-arrow" style="left:268px" width="34" height="28" viewBox="0 0 34 28"><path d="M0 10h20V2l14 12-14 12v-8H0z" fill="#eeeff1"/></svg>
    <div class="step two" style="left:318px">Develop precise, results-driven strategies to drive your company forward</div>
    <svg class="step-arrow" style="left:484px" width="34" height="28" viewBox="0 0 34 28"><path d="M0 10h20V2l14 12-14 12v-8H0z" fill="#eeeff1"/></svg>
    <div class="step three" style="left:532px">Lead your company through transformative processes to achieve tangible success</div>
    <div class="rule"></div>
  </section>

  <section class="section insights-head">
    <h2 class="section-title">TBW Insights &amp; News</h2>
  </section>

  <section class="section insights">
    <article class="news-card" style="left:0;width:194px">
      <div class="photo" role="img" aria-label="Portrait of a businessman with glasses holding a tablet" style="background:linear-gradient(180deg,#8a96a6,#4d5f7c)"></div>
      <div class="shade"></div>
      <div class="news-date">04/05/2023</div>
      <h3 class="news-title">Revolutionizing Business Growth: A Deep Dive into Investment Strategies</h3>
    </article>
    <article class="news-card" style="left:199px;width:190px">
      <div class="photo" role="img" aria-label="Two colleagues reviewing a printed report" style="background:linear-gradient(180deg,#c9ccd0,#6b7688)"></div>
      <div class="shade"></div>
      <div class="news-date">04/05/2023</div>
      <h3 class="news-title" style="top:246px">Revolutionizing Business Growth: A Deep Dive into Investment Strategies</h3>
    </article>
    <article class="news-card" style="left:395px;width:190px">
      <div class="photo" role="img" aria-label="Tablet displaying a line chart" style="background:linear-gradient(180deg,#b8c1cc,#5a6a84)"></div>
      <div class="shade"></div>
      <div class="news-date">04/05/2023</div>
      <h3 class="news-title">Revolutionizing Business Growth: A Deep Dive into Investment Strategies</h3>
    </article>
    <article class="news-card" style="left:590px;width:193px">
      <div class="photo" role="img" aria-label="Two smiling businesswomen in an office" style="background:linear-gradient(180deg,#a9b4b8,#56677f)"></div>
      <div class="shade"></div>
      <div class="news-date">04/05/2023</div>
      <h3 class="news-title">Revolutionizing Business Growth: A Deep Dive into Investment Strategies</h3>
    </article>
  </section>

  <section class="section balance">
    <div class="photo city" role="img" aria-label="City buildings in soft grey haze"></div>
    <div class="photo rail" role="img" aria-label="Railway bridge along the bottom of the scene"></div>
    <svg class="pillar-lines" width="783" height="335" viewBox="0 0 783 335" fill="none" stroke="#9aa3ae" stroke-width=".8">
      <path d="M187 84L266 102M187 147L266 158M187 207L266 206M187 268L266 250"/>
    </svg>
    <div class="pillar" style="top:68px">STRATEGY</div>
    <div class="pillar" style="top:131px">FINANCE</div>
    <div class="pillar" style="top:190px">OPERATIONS</div>
    <div class="pillar" style="top:252px">PARTNERSHIPS</div>
    <div class="balance-panel">
      <div class="kicker">TALLOWBROOK WEALTH PARTNERS:</div>
      <h2>Providing <em>Balance</em> and<br><em>Growth</em> to Your Business</h2>
    </div>
    <div class="photo figure" role="img" aria-label="Businessman in a green shirt balancing with arms outstretched on a rail"></div>
  </section>

  <footer class="section footer">
    <ul class="footer-links">
      <li>Our Approach</li>
      <li>Investment Criteria</li>
      <li>About Us</li>
      <li>Contact Us</li>
    </ul>
    <div class="footer-col" style="left:359px">
      <h4>Our Team</h4>
      <span class="contact">+44 (0)7700 900 314</span><br>
      <span class="contact">inquiries@tallowbrook.example</span>
    </div>
    <div class="footer-col" style="left:564px">
      <h4>Address</h4>
      <address>Tallowbrook Wealth Partners Ltd.<br>Harbourline Centre, Wharf Road,<br>Bridgetown</address>
    </div>
    <div class="footer-base">
      <span>© 2024 Tallowbrook Wealth Partners</span>
      <span>Sitemap &nbsp;|&nbsp; Terms of Use &nbsp;|&nbsp; Privacy Policy &nbsp;|&nbsp; Contact Us</span>
    </div>
  </footer>

</main>
</body>
</html>
```